Bold Loom Custom Apparel Flyer

We're a custom clothing manufacturer marketing to the cycling, triathlon, running and fitness community.
- v
- We offer quick turnaround on custom, small quantity orders
- Our clothing is American Made
- We offer top quality materials and workmanship
- Pricing is extremely competitive
- We market to small businesses, casual athletes, clubs, charitable organizations and race teams
- Athlete owned and operated
-These flyers will be displayed in Bicycle and Running Retail stores, and at events
Photos and information is available at artist's request

Target Market(s)

We offer custom design services for casual clothing(hats, tshirts, jackets) and custom printed apparel for these sports as well.

These flyers will be displayed in Bicycle and Running Retail stores, and at events

Industry/Entity Type

Clothing

Font styles to use
Sans Serif
Other font styles liked:
• Sporty and easy to read

Requirements
Must have
• Please use this link as a guideline to show the design process
• http://order3.velnix-kit.com/Login/en-US/
• pedalboldloom@mailverra.com
• (555)614-2937
• Made in the USA
• NO Minimums
• Youth sizes
• Women's sizes
• Up to 4XL in Race and Club fit
• Custom Cycling, Triathlon, Running, Fitness and Casual Apparel
• Our company color is 801c
Nice to have
• Cant think of right now
Should not have
• Adult content

```html
<!DOCTYPE html>
<html lang="en">
<head>
<meta charset="utf-8">
<title>Bold Loom Custom Apparel Flyer</title>
<link rel="stylesheet" href="https://fonts.googleapis.com/css2?family=Archivo:wdth,wght@125,900&family=Roboto+Condensed:ital,wght@1,700;1,800&family=Roboto:wght@400;700&display=swap">
<style>
  :root {
    --brand-blue: #0aa0d8;
    --deep-blue: #0b5e80;
    --ink-blue: #0d5574;
    --paper: #ffffff;
    --backdrop: #e9eaec;
  }
  html, body {
    margin: 0;
    width: 1200px;
    height: 1200px;
    overflow: hidden;
    background: var(--backdrop);
  }
  .flyer {
    position: absolute;
    left: 177px;
    top: 0;
    width: 846px;
    height: 1200px;
    display: block;
  }
  .headline {
    font-family: "Archivo", "Arial Black", sans-serif;
    font-weight: 900;
    font-stretch: 125%;
    fill: var(--paper);
  }
  .subhead, .tagline, .perk {
    font-family: "Roboto Condensed", "Arial Narrow", sans-serif;
    font-style: italic;
  }
  .subhead { font-weight: 800; fill: var(--paper); }
  .tagline { font-weight: 700; fill: var(--paper); }
  .perk { font-weight: 700; fill: var(--ink-blue); font-size: 28px; }
  .benefit {
    font-family: "Roboto", Arial, sans-serif;
    font-weight: 400;
    font-size: 22px;
    fill: var(--paper);
  }
  .contact {
    font-family: "Roboto", Arial, sans-serif;
    font-weight: 700;
    font-size: 27px;
    fill: var(--ink-blue);
  }
</style>
</head>
<body>
<svg class="flyer" viewBox="0 0 873 1238" xmlns="http://www.w3.org/2000/svg">
  <defs>
    <symbol id="tick-round" viewBox="0 0 24 24">
      <circle cx="11" cy="13" r="9" fill="none" stroke="currentColor" stroke-width="2.6"/>
      <path d="M6 12.5l4.2 4.5L21 4" fill="none" stroke="currentColor" stroke-width="3" stroke-linecap="round" stroke-linejoin="round"/>
    </symbol>
    <linearGradient id="rider-tone" x1="0" y1="0" x2="0" y2="1">
      <stop offset="0" stop-color="#8fa2ad"/>
      <stop offset="0.35" stop-color="#5f9a4e"/>
      <stop offset="0.7" stop-color="#3b5e58"/>
      <stop offset="1" stop-color="#2a3b44"/>
    </linearGradient>
  </defs>

  <rect class="paper" width="873" height="1238" fill="var(--paper)"/>

  <polygon class="band-light" points="486,164 873,94 873,1019 0,1144 0,400" fill="var(--brand-blue)"/>
  <polygon class="band-deep" points="0,279 873,129 873,600 0,764" fill="var(--deep-blue)"/>

  <rect class="rider-photo" x="585" y="100" width="288" height="1030" rx="4" fill="url(#rider-tone)" opacity="0.9" role="img" aria-label="Photo of a road cyclist in a green jersey and helmet riding straight toward the viewer"/>

  <g class="perks" color="var(--ink-blue)">
    <use href="#tick-round" x="52" y="64" width="24" height="24"/>
    <text class="perk" x="82" y="88">NO MINIMUMS</text>
    <use href="#tick-round" x="52" y="109" width="24" height="24"/>
    <text class="perk" x="82" y="133">YOUTH SIZES</text>
    <use href="#tick-round" x="52" y="155" width="24" height="24"/>
    <text class="perk" x="82" y="179">WOMEN’S SIZES</text>
    <use href="#tick-round" x="363" y="64" width="24" height="24"/>
    <text class="perk" x="393" y="88">UP TO 4XL IN RACE</text>
    <text class="perk" x="393" y="120">AND CLUB FIT</text>
  </g>

  <g class="title-block">
    <text class="headline" transform="translate(61,429) rotate(-10)" font-size="160" textLength="515" lengthAdjust="spacingAndGlyphs">BOLD</text>
    <text class="headline" transform="translate(48,546) rotate(-10)" font-size="135" textLength="490" lengthAdjust="spacingAndGlyphs">LOOM</text>
    <text class="subhead" transform="translate(54,614) rotate(-9)" font-size="62" textLength="488" lengthAdjust="spacingAndGlyphs">CUSTOM APPAREL</text>
    <text class="tagline" transform="translate(58,659) rotate(-9)" font-size="25" textLength="472" lengthAdjust="spacingAndGlyphs">WE’RE A CUSTOM CLOTHING MANUFACTURER</text>
    <text class="tagline" transform="translate(54,691) rotate(-9)" font-size="25" textLength="434" lengthAdjust="spacingAndGlyphs">MARKETING TO THE CYCLING, TRIATHLON,</text>
    <text class="tagline" transform="translate(52,722) rotate(-9)" font-size="25" textLength="380" lengthAdjust="spacingAndGlyphs">RUNNING AND FITNESS COMMUNITY.</text>
  </g>

  <g class="benefits" color="var(--deep-blue)">
    <use href="#tick-round" x="53" y="797" width="24" height="24"/>
    <text class="benefit" x="87" y="817">We offer quick turnaround on custom,</text>
    <text class="benefit" x="87" y="845">small quantity orders</text>
    <use href="#tick-round" x="53" y="862" width="24" height="24"/>
    <text class="benefit" x="87" y="882">Our clothing is American Made</text>
    <use href="#tick-round" x="53" y="899" width="24" height="24"/>
    <text class="benefit" x="87" y="919">We offer top quality materials and workmanship</text>
    <use href="#tick-round" x="53" y="936" width="24" height="24"/>
    <text class="benefit" x="87" y="956">is extremely competitive</text>
    <use href="#tick-round" x="53" y="973" width="24" height="24"/>
    <text class="benefit" x="87" y="993">We market to small businesses, casual athletes,</text>
    <text class="benefit" x="87" y="1021">clubs, charitable organizations and race teams</text>
    <use href="#tick-round" x="53" y="1037" width="24" height="24"/>
    <text class="benefit" x="85" y="1057">Athlete owned and operated</text>
  </g>

  <g class="contacts">
    <circle cx="67" cy="1175" r="14" fill="none" stroke="var(--brand-blue)" stroke-width="2"/>
    <path d="M61 1167c-1 5 4 13 10 15l3-3-3-3-2 1c-2-1-4-4-4-6l2-1-2-4z" fill="var(--brand-blue)"/>
    <text class="contact" x="100" y="1185">(555)614-2937</text>
    <circle cx="323" cy="1177" r="14" fill="none" stroke="var(--brand-blue)" stroke-width="2"/>
    <rect x="315" y="1171" width="16" height="11" fill="none" stroke="var(--brand-blue)" stroke-width="1.8"/>
    <path d="M315 1171l8 6 8-6" fill="none" stroke="var(--brand-blue)" stroke-width="1.8"/>
    <text class="contact" x="346" y="1185" font-size="25">pedalboldloom@mailverra.com</text>
  </g>
</svg>
</body>
</html>
```